CINEMA IN CONCERT

We need a need a flyer that will be used to promote a concert.

The concert name will be "Cinema in Concert", this flyer needs to appeal to all
ages becuase we are playing music from movies such as moon raiders, montana briggs Felix Tumbler and more. I would also like a photo of an orchestra in background so people know there is an actual orchestra playing.

If you use photos from the movies please make sure, I do not have any issues with rights to the photo.

Please make sure to add info into flyer.

"Cinema in Concert"

Location: Brennock Auditorium

Date: September 22nd, 2013 - Sunday

Time: 3:00pm                                   

Target Market(s)

All Audience young and old

Requirements
Must have
• "Cinema in Concert"
• Location: Brennock Auditorium
• Date: September 22nd, 2013 - Sunday
• Time: 3:00pm

```html
<!DOCTYPE html>
<html lang="en">
<head>
<meta charset="utf-8">
<title>Cinema in Concert</title>
<link rel="stylesheet" href="https://fonts.googleapis.com/css2?family=Bangers&family=Bebas+Neue&display=swap">
<style>
  :root {
    --crimson: #800000;
    --crimson-deep: #5a0404;
    --crimson-dark: #350707;
    --ink: #000000;
    --paper: #ffffff;
    --burst-text: #ffff00;
  }
  * { margin: 0; padding: 0; box-sizing: border-box; }
  html, body { width: 848px; height: 1200px; overflow: hidden; background: var(--paper); }
  .flyer {
    position: relative;
    width: 848px;
    height: 1200px;
    overflow: hidden;
    background: var(--paper);
    font-family: "Bebas Neue", "Arial Narrow", sans-serif;
    color: var(--ink);
  }
  .masthead {
    position: absolute; left: 0; top: 0; width: 848px; height: 335px;
    background: var(--crimson);
  }
  .band-deep { position: absolute; left: 0; top: 335px; width: 848px; height: 31px; background: var(--crimson-deep); }
  .band-dark { position: absolute; left: 0; top: 366px; width: 848px; height: 30px; background: var(--crimson-dark); }
  .star { position: absolute; width: 190px; height: 190px; }
  .star--left { left: 4px; top: 0; }
  .star--right { left: 659px; top: 0; }
  .title-word {
    position: absolute; left: 0; width: 848px; text-align: center;
    line-height: 1; white-space: nowrap;
  }
  .title-word--cinema { top: -6px; font-size: 158px; color: var(--paper); padding-left: 0; padding-right: 14px; }
  .title-word--in { top: 128px; font-size: 104px; color: var(--ink); }
  .title-word--concert { top: 203px; font-size: 158px; color: var(--paper); padding-left: 8px; }
  .details { position: absolute; left: 9px; top: 0; }
  .details-line {
    position: absolute; left: 0; white-space: nowrap;
    font-size: 57px; line-height: 1;
    transform-origin: left top;
  }
  .details-line--1 { top: 405px; transform: scaleX(0.87); }
  .details-line--2 { top: 476px; transform: scaleX(0.866); }
  .details-line--3 { top: 542px; transform: scaleX(0.767); }
  .details-line--4 { top: 609px; font-size: 63px; transform: scaleX(0.636); }
  .details-line--5 { top: 692px; font-size: 63px; transform: scaleX(0.628); }
  .details-line--6 { top: 789px; font-size: 63px; transform: scaleX(0.628); }
  .conductor {
    position: absolute; left: 283px; top: 782px; width: 255px; height: 418px;
    background: var(--ink);
    border-radius: 110px 110px 0 0;
  }
  .burst { position: absolute; width: 340px; height: 340px; }
  .burst--live { left: -10px; top: 862px; }
  .burst--ages { left: 489px; top: 857px; }
  .burst-label {
    position: absolute; font-family: "Bangers", "Impact", cursive;
    color: var(--burst-text); line-height: 1; text-align: center; white-space: nowrap;
  }
  .burst-label--live { left: 103px; top: 993px; font-size: 84px; transform: rotate(-9deg) scaleX(1.3); }
  .burst-label--ages { left: 565px; top: 953px; font-size: 52px; line-height: 1.25; transform: rotate(15deg) scaleX(1.15); }
</style>
</head>
<body>
<main class="flyer">
  <header class="masthead">
    <svg class="star star--left" viewBox="-100 -100 200 200" aria-hidden="true">
      <polygon fill="#ffffff" points="0,-100 22,-31 95,-31 36,12 59,81 0,38 -59,81 -36,12 -95,-31 -22,-31"/>
    </svg>
    <svg class="star star--right" viewBox="-100 -100 200 200" aria-hidden="true">
      <polygon fill="#ffffff" points="0,-100 22,-31 95,-31 36,12 59,81 0,38 -59,81 -36,12 -95,-31 -22,-31"/>
    </svg>
    <h1>
      <span class="title-word title-word--cinema">Cinema</span>
      <span class="title-word title-word--in">In</span>
      <span class="title-word title-word--concert">Concert</span>
    </h1>
  </header>
  <div class="band-deep"></div>
  <div class="band-dark"></div>

  <section class="details">
    <p class="details-line details-line--1">COME SEE A LIVE ORCHESTRA PERFORM SOME</p>
    <p class="details-line details-line--2">OF THE MOST KNOWN MOVIE SCORES EVER PRODUCED</p>
    <p class="details-line details-line--3">SUCH AS FELIX TUMBLER, MOON RAIDERS, AND MONTANA BRIGGS</p>
    <p class="details-line details-line--4">THE CINEMA IN CONCERT WILL BE HELD IN THE BRENNOCK AUDITORIUM</p>
    <p class="details-line details-line--5">ON SUNDAY, SEPTEMBER 22ND 2013. THE PERFORMANCE WILL BE HELD</p>
    <p class="details-line details-line--6">AT 3:00 PM.</p>
  </section>

  <svg class="burst burst--live" viewBox="-170 -170 340 340" aria-hidden="true">
    <polygon fill="#800000" points="165,0 92,25 143,83 67,67 83,143 25,92 0,165 -25,92 -83,143 -67,67 -143,83 -92,25 -165,0 -92,-25 -143,-83 -67,-67 -83,-143 -25,-92 0,-165 25,-92 83,-143 67,-67 143,-83 92,-25"/>
  </svg>
  <svg class="burst burst--ages" viewBox="-170 -170 340 340" aria-hidden="true">
    <polygon fill="#800000" points="165,0 92,25 143,83 67,67 83,143 25,92 0,165 -25,92 -83,143 -67,67 -143,83 -92,25 -165,0 -92,-25 -143,-83 -67,-67 -83,-143 -25,-92 0,-165 25,-92 83,-143 67,-67 143,-83 92,-25"/>
  </svg>

  <div class="conductor" role="img" aria-label="Black silhouette of an orchestra conductor with both arms raised"></div>

  <p class="burst-label burst-label--live">LIVE!</p>
  <p class="burst-label burst-label--ages">ALL AGES<br>WELCOME!</p>
</main>
</body>
</html>
```